Korvane blockchain

A Blockchain investment company template for a switzerland based company. The company is also offering its own blockchain infrastructure in partnership with a top 200 blockchain project, on which blockchain startups can develop their ideas.
In addition, co-working spaces are offered in an innovation center.
So these three parts should be covered in the template

1. Crypto investment
2. Offering the blockchain infrastructure
3. Co-working spaces (https://travelnix.example/)

Target Market(s)

Blockchain / Crypto

Colors
ec1f27

Requirements
Must have
• Connection to the three parts mentioned in the description
inculding to logo attached
Nice to have
• connection to switzerland

```html
<!DOCTYPE html>
<html lang="en">
<head>
<meta charset="utf-8">
<title>Korvane blockchain – Presentation Template</title>
<link href="https://fonts.googleapis.com/css2?family=Montserrat:wght@400;500;600;700;800&family=Roboto+Condensed:wght@700&family=Poppins:wght@400;500;600&display=swap" rel="stylesheet">
<style>
:root{
  --red:#ec1f27;
  --ink:#221f20;
  --ink-deep:#151313;
  --text:#3a3a3a;
  --muted:#8a8a8a;
  --line:#e3e3e3;
  --paper:#ffffff;
  --canvas:#eef0f2;
  --pink:#fbe3e4;
}
*{margin:0;padding:0;box-sizing:border-box}
html,body{width:1200px;height:3873px;overflow:hidden}
body{background:var(--paper);font-family:"Poppins",sans-serif;color:var(--text);position:relative}
.stage{position:absolute;left:0;top:0;width:1200px;height:790px;background:linear-gradient(180deg,#dfe2e5 0%,#eef0f2 60%,#ffffff 100%)}
.hero-wrap{position:absolute;left:232px;top:170px;width:566px;height:319px;transform:scale(1.3);transform-origin:0 0;box-shadow:0 20px 40px rgba(0,0,0,.25)}
.slide{position:absolute;width:566px;height:319px;overflow:hidden;background:var(--paper);box-shadow:0 2px 8px rgba(0,0,0,.18)}
.abs{position:absolute}
.dark{background:var(--ink);color:#fff}
.photo{position:absolute}
.brand{position:absolute;display:flex;align-items:center;gap:4px;font-family:"Montserrat",sans-serif;font-weight:600;font-size:11px;color:var(--red);white-space:nowrap}
.brand-mark{width:9px;height:9px;background:var(--red);display:inline-block}
.brand.center{flex-direction:column;gap:5px;transform:translateX(-50%)}
.brand.center .brand-mark{width:22px;height:22px}
.corner-mark{position:absolute;left:10px;top:14px;width:10px;height:10px;border:2px solid var(--red)}
.copyright{position:absolute;left:6px;top:160px;transform:rotate(-90deg);transform-origin:0 0;font-family:"Montserrat",sans-serif;font-size:4.5px;letter-spacing:1px;color:var(--muted);white-space:nowrap}
.page-no{position:absolute;left:10px;bottom:10px;width:13px;height:13px;border-radius:50%;background:var(--red);color:#fff;font-size:5px;line-height:13px;text-align:center;font-weight:600}
.t-main{font-family:"Montserrat",sans-serif;font-weight:800;line-height:1;letter-spacing:-.5px}
.t-cond{font-family:"Roboto Condensed",sans-serif;font-weight:700;line-height:1}
.t-sub{font-family:"Montserrat",sans-serif;font-weight:400;letter-spacing:2px;line-height:1}
.pill{position:absolute;background:var(--red);color:#fff;border-radius:20px;text-align:center;font-family:"Montserrat",sans-serif;font-weight:600}
.pill.web{font-size:6px;letter-spacing:1.5px;font-weight:700}
.title{font-family:"Montserrat",sans-serif;font-weight:600;color:var(--ink);line-height:1.15}
.red{color:var(--red)}
.small{font-size:5.2px;line-height:1.45;color:#555}
.tiny{font-size:4.6px;line-height:1.4;color:#666}
.bold{font-weight:600;color:var(--ink)}
.rule-top{position:absolute;left:0;top:0;width:100%;height:3px;background:var(--red)}
.rule-bot{position:absolute;left:0;bottom:0;width:100%;height:3px;background:var(--red)}
.agenda-item{position:absolute;left:310px;width:205px;height:22px;border-bottom:1px solid var(--line);font-size:7px;color:#555;display:flex;align-items:flex-end;padding-bottom:4px}
.agenda-item b{width:35px;color:var(--red);font-weight:400;font-family:"Times New Roman",serif;font-style:italic}
.dot-list li{list-style:none;position:relative;padding-left:9px;margin-bottom:4px}
.dot-list li::before{content:"";position:absolute;left:0;top:1px;width:5px;height:5px;border-radius:50%;background:var(--red)}
.feature{position:absolute;width:120px;height:104px;background:var(--ink-deep);padding:10px 9px;color:#ccc}
.feature h4{font-size:6px;color:#fff;font-weight:500;margin:5px 0 3px}
.feature .bar{width:16px;height:1.5px;background:var(--red);margin-bottom:5px}
.feature .tiny{color:#aaa}
.icon-ring{width:14px;height:14px;border:1.2px solid #ddd;border-radius:50%}
.card{position:absolute;width:152px;height:80px;border:1px solid #f2c4c6;border-radius:4px;background:#fff;box-shadow:0 2px 5px rgba(236,31,39,.12);padding:14px 8px 0 50px}
.card svg{position:absolute;left:14px;top:20px}
.card h5{font-size:7px;font-weight:600;color:var(--ink);margin-bottom:3px}
.list-row{position:absolute;width:200px;padding-left:42px}
.list-row .bub{position:absolute;left:0;top:0;width:28px;height:28px;border-radius:50%;background:var(--red);box-shadow:0 0 0 3px #fde0e1}
.list-row h5{font-size:7px;font-weight:600;color:var(--ink);margin-bottom:2px}
.circ{position:absolute;width:46px;height:46px;border-radius:50%;background:var(--red);border:3px solid #fff;box-shadow:0 2px 6px rgba(0,0,0,.25)}
.col3{position:absolute;width:140px;text-align:center}
.col3 h5{font-size:7.5px;font-weight:600;color:var(--ink);margin-bottom:3px}
.badge{position:absolute;width:64px;height:30px;background:#fff;border:1px solid #f3c9cb;border-radius:3px;box-shadow:0 1px 4px rgba(0,0,0,.08)}
.badge i{position:absolute;left:14px;top:12px;width:36px;height:6px;background:#d9d9d9;border-radius:2px}
.tbl-head{position:absolute;left:200px;top:78px;width:352px;height:22px;background:var(--red);display:flex}
.tbl-head span,.tbl-row span{flex:1;text-align:center;font-size:5.5px;line-height:22px}
.tbl-head span{color:#fff;font-weight:600}
.tbl-row{position:absolute;left:45px;width:507px;height:24px;display:flex}
.tbl-row .lab{flex:0 0 155px;background:var(--ink);color:#fff;font-weight:600;font-size:5px;line-height:22px;margin-bottom:2px;text-align:center}
.tbl-row span{color:#555;line-height:24px}
.ok{color:var(--red);font-weight:700}
.no{color:var(--red);font-weight:700}
.tl-text{position:absolute;width:90px;text-align:center;transform:translateX(-50%)}
.tl-text h6{font-size:6px;font-weight:600;color:var(--ink)}
.tl-pin{position:absolute;width:1.2px;height:22px;background:var(--ink);transform:translateX(-50%)}
.tl-year{position:absolute;top:177px;font-size:7px;font-weight:600;color:#fff;transform:translateX(-50%)}
.pie-text{position:absolute;width:120px}
.pie-text h6{font-size:6.5px;font-weight:600;color:var(--ink);margin-bottom:2px}
.contact-line{position:absolute;left:52px;display:flex;align-items:center;gap:8px;font-size:5.5px;color:#ddd}
.contact-line i{width:11px;height:11px;border-radius:50%;background:var(--red);display:inline-block}
</style>
</head>
<body>

<!-- Showcase area -->
<section class="stage">
  <div class="hero-wrap">
    <div class="slide" style="left:0;top:0">
      <div class="photo" role="img" aria-label="Close-up of a hand holding a gold coin against a dark background" style="left:0;top:0;width:566px;height:250px;background:radial-gradient(ellipse at 70% 45%,#5a4a44 0%,#332a28 40%,#1f1a1a 100%)"></div>
      <div class="pill web" style="left:44px;top:64px;width:165px;height:16px;line-height:16px">WWW.WEBSITENAME.COM</div>
      <div class="abs" style="left:42px;top:112px;color:#fff">
        <div class="t-main" style="font-size:38px">PRESENTATION</div>
        <div class="t-cond" style="font-size:27px">TITLE GOES HERE</div>
        <div class="t-sub" style="font-size:14px;letter-spacing:1.5px;margin-top:2px">Sub Title Goes Here</div>
      </div>
      <div class="pill" style="left:388px;top:236px;width:160px;height:22px;line-height:22px;font-size:8px">March 2021</div>
      <div class="brand" style="left:36px;top:286px"><span class="brand-mark"></span>Korvane blockchain</div>
    </div>
  </div>
</section>

<!-- Row 1 -->
<div class="slide dark" style="left:24px;top:824px">
  <div class="rule-top"></div><div class="rule-bot"></div>
  <div class="brand center" style="left:283px;top:50px"><span class="brand-mark"></span>Korvane blockchain</div>
  <div class="abs" style="left:0;width:566px;top:128px;text-align:center">
    <div class="t-main" style="font-size:37px">PRESENTATION</div>
    <div class="t-cond" style="font-size:24px">TITLE GOES HERE</div>
    <div class="t-sub red" style="font-size:13px;margin-top:1px">Sub Title Goes Here</div>
  </div>
  <div class="pill" style="left:214px;top:243px;width:138px;height:20px;line-height:20px;font-size:8px;font-weight:500">Presenter Name</div>
</div>

<div class="slide" style="left:618px;top:824px">
  <div class="rule-top"></div><div class="rule-bot"></div>
  <div class="brand center" style="left:283px;top:42px"><span class="brand-mark"></span>Korvane blockchain</div>
  <div class="abs" style="left:0;width:566px;top:132px;text-align:center;color:var(--ink)">
    <div class="t-main" style="font-size:37px">PRESENTATION</div>
    <div class="t-cond" style="font-size:24px">TITLE GOES HERE</div>
    <div class="t-sub red" style="font-size:13px;margin-top:1px">Sub Title Goes Here</div>
  </div>
  <div class="pill" style="left:214px;top:252px;width:138px;height:20px;line-height:20px;font-size:8px;font-weight:500">Presenter Name</div>
</div>

<!-- Row 2 -->
<div class="slide" style="left:24px;top:1166px">
  <div class="photo" role="img" aria-label="Hiker in a red jacket standing before a snowy Swiss mountain peak" style="left:0;top:0;width:270px;height:319px;background:linear-gradient(180deg,#ffffff 0%,#e9eef3 45%,#b9c4ce 75%,#dfe5ea 100%)"></div>
  <div class="brand center" style="left:300px;top:68px;font-size:8px"><span class="brand-mark" style="width:16px;height:16px"></span>Korvane blockchain</div>
  <div class="abs" style="left:256px;top:136px;color:var(--ink)">
    <div class="t-main" style="font-size:30px">PRESENTATION</div>
    <div class="t-cond" style="font-size:22px">TITLE GOES HERE</div>
    <div class="t-sub red" style="font-size:11px;margin-top:2px">Sub Title Goes Here</div>
  </div>
  <div class="abs" style="left:256px;top:240px;font-size:5px;letter-spacing:1.5px;font-weight:600;color:var(--ink)">WWW.WEBSITE.COM</div>
</div>

<div class="slide dark" style="left:618px;top:1166px">
  <div class="photo" role="img" aria-label="Dark moody panorama of Swiss alpine peaks" style="left:0;top:0;width:566px;height:319px;background:linear-gradient(180deg,#2c2b2d 0%,#4a4a4d 45%,#2a292b 80%,#1d1c1d 100%)"></div>
  <div class="brand" style="left:34px;top:58px;font-size:9px"><span class="brand-mark"></span>Korvane blockchain</div>
  <div class="abs" style="left:33px;top:142px">
    <div class="t-main" style="font-size:37px">PRESENTATION</div>
    <div class="t-cond" style="font-size:27px">TITLE GOES HERE</div>
    <div class="t-sub" style="font-size:14px">Sub Title Goes Here</div>
  </div>
  <div class="pill web" style="left:33px;top:260px;width:140px;height:15px;line-height:15px;font-size:5px">WWW.WEBSITENAME.COM</div>
</div>

<!-- Row 3 -->
<div class="slide" style="left:24px;top:1498px">
  <div class="photo" role="img" aria-label="Close-up of a hand holding a gold coin against a dark background" style="left:0;top:0;width:566px;height:248px;background:radial-gradient(ellipse at 70% 45%,#5a4a44 0%,#332a28 40%,#1f1a1a 100%)"></div>
  <div class="pill web" style="left:44px;top:64px;width:165px;height:16px;line-height:16px">WWW.WEBSITENAME.COM</div>
  <div class="abs" style="left:42px;top:112px;color:#fff">
    <div class="t-main" style="font-size:38px">PRESENTATION</div>
    <div class="t-cond" style="font-size:27px">TITLE GOES HERE</div>
    <div class="t-sub" style="font-size:14px;letter-spacing:1.5px;margin-top:2px">Sub Title Goes Here</div>
  </div>
  <div class="pill" style="left:388px;top:236px;width:160px;height:22px;line-height:22px;font-size:8px">March 2021</div>
  <div class="brand" style="left:36px;top:286px"><span class="brand-mark"></span>Korvane blockchain</div>
</div>

<div class="slide" style="left:618px;top:1498px">
  <span class="corner-mark"></span><span class="copyright">COPYRIGHT © 2021</span><span class="page-no">7</span>
  <div class="abs title" style="left:66px;top:116px;font-size:20px">Here Goes<br>Title Of Your<br>Agenda</div>
  <div class="abs red" style="left:66px;top:194px;font-size:8px;font-weight:600">Here Goes A Short Subtitle</div>
  <div class="agenda-item" style="top:56px"><b>i.</b>Introduction</div>
  <div class="agenda-item" style="top:78px"><b>ii.</b>About Us</div>
  <div class="agenda-item" style="top:100px"><b>iii.</b>Welcome Message</div>
  <div class="agenda-item" style="top:122px"><b>iv.</b>Company Profile</div>
  <div class="agenda-item" style="top:144px"><b>v.</b>Team</div>
  <div class="agenda-item" style="top:166px"><b>vi.</b>Team Group</div>
  <div class="agenda-item" style="top:188px"><b>vii.</b>Portfolio</div>
  <div class="agenda-item" style="top:210px"><b>viii.</b>Info graphic</div>
  <div class="agenda-item" style="top:232px"><b>ix.</b>Contact Us</div>
</div>

<!-- Row 4 -->
<div class="slide" style="left:24px;top:1832px">
  <span class="corner-mark"></span><span class="copyright">COPYRIGHT © 2021</span><span class="page-no">8</span>
  <div class="abs" style="left:430px;top:0;width:136px;height:319px;background:var(--red)"></div>
  <div class="abs title" style="left:50px;top:36px;font-size:21px">Das Basecamp für<br>Innovationen.</div>
  <div class="abs red" style="left:50px;top:88px;font-size:7.5px;font-weight:600">Eine Welt für Kreativität &amp; Begegnung.</div>
  <p class="abs small" style="left:50px;top:102px;width:215px">Lorem ipsum dolor sit amet, consectetur adipiscing elit, sed do eiusmod tempor incididunt ut labore et dolore magna aliqua. Ut enim ad minim veniam, quis nostrud exercitation ullamco laboris nisi ut aliquip ex ea commodo consequat duis aute irure.</p>
  <ul class="abs small dot-list" style="left:50px;top:182px;width:215px">
    <li>Lorem ipsum dolor sit amet, consectetur adipiscing</li>
    <li>Sed do eiusmod tempor incididunt ut labore et</li>
    <li>Dolore magna aliqua. Ut enim ad minim veniam</li>
    <li>Quis nostrud exercitation ullamco laboris nisi ut</li>
  </ul>
  <div class="photo" role="img" aria-label="Modern glass innovation centre building with a car parked in front and mountains behind" style="left:296px;top:72px;width:244px;height:184px;border-radius:8px;box-shadow:0 4px 12px rgba(0,0,0,.3);background:linear-gradient(180deg,#dfe9f1 0%,#c9d7e0 40%,#8c9795 60%,#6d7668 80%,#9da19b 100%)"></div>
</div>

<div class="slide" style="left:618px;top:1832px">
  <span class="corner-mark"></span><span class="copyright">COPYRIGHT © 2021</span><span class="page-no">9</span>
  <div class="abs title" style="left:45px;top:56px;font-size:23px">Here Goes<br><span class="red">Title Of This Slide</span></div>
  <div class="abs bold" style="left:45px;top:132px;font-size:7.5px">Your Short Text Here</div>
  <p class="abs small" style="left:45px;top:154px;width:142px;text-align:justify">Lorem ipsum dolor sit amet, consectetur adipiscing elit, sed do eiusmod tempor incididunt ut labore et dolore magna aliqua. Lorem ipsum dolor sit amet.<br><br>Sed do eiusmod tempor incididunt ut labore et dolore magna aliqua.<br><br>Ut enim ad minim veniam, quis nostrud exercitation ullamco laboris nisi ut aliquip.</p>
  <p class="abs small" style="left:218px;top:154px;width:142px;text-align:justify">Lorem ipsum dolor sit amet, consectetur adipiscing elit, sed do eiusmod tempor incididunt ut labore et dolore magna aliqua. Lorem ipsum dolor sit amet.<br><br>Consectetur adipiscing elit, sed do eiusmod tempor incididunt ut labore et dolore magna aliqua. Ut enim ad minim veniam, quis nostrud exercitation ullamco laboris nisi ut aliquip.</p>
  <p class="abs small" style="left:390px;top:154px;width:142px;text-align:justify">Lorem ipsum dolor sit amet, consectetur adipiscing elit, sed do eiusmod tempor incididunt ut labore et dolore magna aliqua. Lorem ipsum dolor sit amet.<br><br>Consectetur adipiscing elit, sed do eiusmod tempor incididunt ut labore et dolore magna aliqua.<br><br>Ut enim ad minim veniam, quis nostrud exercitation ullamco laboris nisi ut aliquip.</p>
</div>

<!-- Row 5 -->
<div class="slide dark" style="left:24px;top:2170px">
  <div class="photo" role="img" aria-label="Hand holding a gold coin against a dark blurred background" style="left:0;top:0;width:240px;height:319px;background:radial-gradient(ellipse at 45% 55%,#7a6a5c 0%,#3f3834 40%,#1f1c1d 100%)"></div>
  <div class="abs" style="left:262px;top:94px;font-family:Montserrat,sans-serif;font-weight:600;font-size:22px">Cryptocurrency</div>
  <p class="abs tiny" style="left:262px;top:124px;width:275px;color:#ddd;font-size:5.6px;text-align:justify">Lorem ipsum dolor sit amet, consectetur adipiscing elit, sed do eiusmod tempor incididunt ut labore et dolore magna aliqua. Lorem ipsum dolor sit amet, consectetur adipiscing elit. Sed do eiusmod tempor incididunt ut labore et dolore magna aliqua. Ut enim ad minim veniam, quis nostrud exercitation ullamco laboris.</p>
  <div class="feature" style="left:160px;top:180px"><div class="icon-ring"></div><h4>Currency</h4><div class="bar"></div><p class="tiny">Lorem ipsum dolor sit amet, consectetur adipiscing elit, sed do eiusmod tempor incididunt ut labore et dolore magna.</p></div>
  <div class="feature" style="left:290px;top:180px"><div class="icon-ring"></div><h4>Dedication</h4><div class="bar"></div><p class="tiny">Lorem ipsum dolor sit amet, consectetur adipiscing elit, sed do eiusmod tempor incididunt ut labore et dolore magna.</p></div>
  <div class="feature" style="left:420px;top:180px"><div class="icon-ring"></div><h4>Customer Focus</h4><div class="bar"></div><p class="tiny">Lorem ipsum dolor sit amet, consectetur adipiscing elit, sed do eiusmod tempor incididunt ut labore et dolore magna.</p></div>
</div>

<div class="slide" style="left:618px;top:2170px">
  <span class="corner-mark"></span><span class="copyright">COPYRIGHT © 2021</span><span class="page-no">11</span>
  <div class="abs title" style="left:54px;top:48px;font-size:20px">Your Title Here</div>
  <div class="card" style="left:48px;top:96px"><svg width="24" height="24" viewBox="0 0 24 24" fill="none" stroke="#ec1f27" stroke-width="1.4"><circle cx="12" cy="12" r="5"/><circle cx="12" cy="12" r="10"/></svg><h5>Project name</h5><p class="tiny">Lorem ipsum is simply dummy text of the print and type setting trade.</p></div>
  <div class="card" style="left:213px;top:96px"><svg width="24" height="24" viewBox="0 0 24 24" fill="none" stroke="#ec1f27" stroke-width="1.4"><circle cx="9" cy="9" r="6"/><path d="M13 13l8 8"/></svg><h5>Project name</h5><p class="tiny">Lorem ipsum is simply dummy text of the print and type setting trade.</p></div>
  <div class="card" style="left:378px;top:96px"><svg width="24" height="24" viewBox="0 0 24 24" fill="none" stroke="#ec1f27" stroke-width="1.4"><rect x="3" y="3" width="18" height="18" rx="2"/><path d="M7 9h10M7 13h10M7 17h6"/></svg><h5>Project name</h5><p class="tiny">Lorem ipsum is simply dummy text of the print and type setting trade.</p></div>
  <div class="card" style="left:48px;top:194px"><svg width="24" height="24" viewBox="0 0 24 24" fill="none" stroke="#ec1f27" stroke-width="1.4"><path d="M12 2l9 5v10l-9 5-9-5V7z"/></svg><h5>Project name</h5><p class="tiny">Lorem ipsum is simply dummy text of the print and type setting trade.</p></div>
  <div class="card" style="left:213px;top:194px"><svg width="24" height="24" viewBox="0 0 24 24" fill="none" stroke="#ec1f27" stroke-width="1.4"><circle cx="7" cy="8" r="3"/><circle cx="17" cy="8" r="3"/><path d="M2 20c0-4 3-6 5-6s5 2 5 6M12 20c0-4 3-6 5-6s5 2 5 6"/></svg><h5>Project name</h5><p class="tiny">Lorem ipsum is simply dummy text of the print and type setting trade.</p></div>
  <div class="card" style="left:378px;top:194px"><svg width="24" height="24" viewBox="0 0 24 24" fill="none" stroke="#ec1f27" stroke-width="1.4"><circle cx="12" cy="10" r="6"/><path d="M9 18h6M10 21h4"/></svg><h5>Project name</h5><p class="tiny">Lorem ipsum is simply dummy text of the print and type setting trade.</p></div>
</div>

<!-- Row 6 -->
<div class="slide" style="left:24px;top:2512px">
  <span class="corner-mark"></span><span class="copyright">COPYRIGHT © 2021</span><span class="page-no">13</span>
  <div class="abs title" style="left:54px;top:44px;font-size:20px">Your Title Here</div>
  <div class="list-row" style="left:54px;top:98px"><span class="bub"></span><h5>Project name</h5><p class="tiny">Lorem ipsum dolor sit amet, nec an dictas equidem appellantur, ut has commune accommodare.</p></div>
  <div class="list-row" style="left:300px;top:98px"><span class="bub"></span><h5>Project name</h5><p class="tiny">Lorem ipsum dolor sit amet, nec an dictas equidem appellantur, ut has commune accommodare.</p></div>
  <div class="list-row" style="left:54px;top:158px"><span class="bub"></span><h5>Project name</h5><p class="tiny">Lorem ipsum dolor sit amet, nec an dictas equidem appellantur, ut has commune accommodare.</p></div>
  <div class="list-row" style="left:300px;top:158px"><span class="bub"></span><h5>Project name</h5><p class="tiny">Lorem ipsum dolor sit amet, nec an dictas equidem appellantur, ut has commune accommodare.</p></div>
  <div class="list-row" style="left:54px;top:218px"><span class="bub"></span><h5>Project name</h5><p class="tiny">Lorem ipsum dolor sit amet, nec an dictas equidem appellantur, ut has commune accommodare.</p></div>
  <div class="list-row" style="left:300px;top:218px"><span class="bub"></span><h5>Project name</h5><p class="tiny">Lorem ipsum dolor sit amet, nec an dictas equidem appellantur, ut has commune accommodare.</p></div>
</div>

<div class="slide" style="left:618px;top:2512px">
  <span class="corner-mark"></span><span class="copyright">COPYRIGHT © 2021</span><span class="page-no">14</span>
  <div class="photo" role="img" aria-label="Dark mountain ridge panorama" style="left:30px;top:0;width:536px;height:160px;background:linear-gradient(180deg,#3a393b 0%,#2a292b 60%,#1f1e1f 100%)"></div>
  <div class="abs" style="left:30px;width:536px;top:36px;text-align:center;color:#fff">
    <div style="font-family:Montserrat,sans-serif;font-weight:600;font-size:18px">Here Add Awesome Text</div>
    <div class="red" style="font-size:9px;font-style:italic;margin-top:2px">Write here a great subtitle</div>
    <p class="tiny" style="color:#ddd;width:370px;margin:6px auto 0;font-size:5.6px">Lorem ipsum dolor sit amet, consectetur adipiscing elit, sed do eiusmod tempor incididunt ut labore et dolore magna aliqua. Lorem ipsum dolor sit amet, consectetur adipiscing elit.</p>
  </div>
  <div class="circ" style="left:94px;top:132px"></div>
  <div class="circ" style="left:264px;top:132px"></div>
  <div class="circ" style="left:434px;top:132px"></div>
  <div class="col3" style="left:47px;top:190px"><h5>Project name</h5><p class="tiny" style="text-align:justify">Lorem ipsum dolor sit amet, nec an dictas equidem appellantur, ut has the same but eco commune accommodare. Mea illum, ludus solet idpro.</p></div>
  <div class="col3" style="left:217px;top:180px"><h5>Project name</h5><p class="tiny" style="text-align:justify">Lorem ipsum dolor sit amet, nec an dictas equidem appellantur, ut has the same but eco commune accommodare. Mea illum, ludus solet idpro.</p></div>
  <div class="col3" style="left:387px;top:180px"><h5>Project name</h5><p class="tiny" style="text-align:justify">Lorem ipsum dolor sit amet, nec an dictas equidem appellantur, ut has the same but eco commune accommodare. Mea illum, ludus solet idpro.</p></div>
</div>

<!-- Row 7 -->
<div class="slide" style="left:24px;top:2850px">
  <span class="corner-mark"></span><span class="copyright">COPYRIGHT © 2021</span><span class="page-no">15</span>
  <div class="abs" style="left:30px;top:134px;width:536px;height:185px;background:var(--ink)"></div>
  <div class="abs title" style="left:62px;top:62px;font-size:21px">Place for the<br>ScreenShot</div>
  <div class="abs red" style="left:62px;top:136px;font-size:7px;line-height:1.4">No problem is too big or too small!<br><b>We're here to help.</b></div>
  <p class="abs tiny" style="left:62px;top:196px;width:210px;color:#ddd;font-size:5.8px;text-align:justify">Lorem ipsum dolor sit amet, consectetur adipiscing elit, sed do eiusmod tempor incididunt ut labore et dolore magna aliqua. Lorem ipsum dolor sit amet, consectetur adipiscing elit. Sed do eiusmod tempor incididunt ut labore et dolore magna aliqua. Ut enim ad minim veniam, quis nostrud exercitation ullamco laboris nisi ut aliquip.</p>
  <div class="abs" style="left:290px;top:80px;width:256px;height:172px;background:#2b2b2b;border-radius:4px;box-shadow:0 4px 12px rgba(0,0,0,.4)">
    <div style="height:12px;display:flex;gap:3px;padding:4px 6px"><i style="width:4px;height:4px;border-radius:50%;background:#ec1f27"></i><i style="width:4px;height:4px;border-radius:50%;background:#f5b400"></i><i style="width:4px;height:4px;border-radius:50%;background:#3ac14a"></i></div>
    <div role="img" aria-label="Screenshot placeholder showing a computer circuit board with a coin" style="margin:0 4px;height:156px;background:linear-gradient(135deg,#d9d9d9 0%,#6e6e6e 40%,#2c2c2c 70%,#8f7b5c 100%)"></div>
  </div>
</div>

<div class="slide" style="left:618px;top:2850px">
  <span class="corner-mark"></span><span class="copyright">COPYRIGHT © 2021</span><span class="page-no">17</span>
  <div class="abs title" style="left:48px;top:150px;font-size:20px">Unsere Partner</div>
  <div class="badge" style="left:251px;top:56px"><i></i></div><div class="badge" style="left:323px;top:56px"><i></i></div><div class="badge" style="left:395px;top:56px"><i></i></div><div class="badge" style="left:467px;top:56px"><i></i></div>
  <div class="badge" style="left:251px;top:100px"><i></i></div><div class="badge" style="left:323px;top:100px"><i></i></div><div class="badge" style="left:395px;top:100px"><i></i></div><div class="badge" style="left:467px;top:100px"><i></i></div>
  <div class="badge" style="left:251px;top:144px"><i></i></div><div class="badge" style="left:323px;top:144px"><i></i></div><div class="badge" style="left:395px;top:144px"><i></i></div><div class="badge" style="left:467px;top:144px"><i></i></div>
  <div class="badge" style="left:251px;top:188px"><i></i></div><div class="badge" style="left:323px;top:188px"><i></i></div><div class="badge" style="left:395px;top:188px"><i></i></div><div class="badge" style="left:467px;top:188px"><i></i></div>
  <div class="badge" style="left:251px;top:232px"><i></i></div><div class="badge" style="left:323px;top:232px"><i></i></div><div class="badge" style="left:395px;top:232px"><i></i></div><div class="badge" style="left:467px;top:232px"><i></i></div>
</div>

<!-- Row 8 -->
<div class="slide" style="left:24px;top:3184px">
  <span class="corner-mark"></span><span class="copyright">COPYRIGHT © 2021</span><span class="page-no">18</span>
  <div class="abs title" style="left:45px;top:36px;font-size:20px">Here Goes Title Of This Slide</div>
  <div class="tbl-head"><span>Your Text Here</span><span>Your Text Here</span><span>Your Text Here</span><span>Your Text Here</span></div>
  <div class="tbl-row" style="top:106px"><span class="lab">You can replace this text</span><span>1250</span><span class="ok">✓</span><span>50%</span><span>1250</span></div>
  <div class="tbl-row" style="top:130px"><span class="lab">You can replace this text</span><span>3623</span><span class="no">✕</span><span>50%</span><span>3623</span></div>
  <div class="tbl-row" style="top:154px"><span class="lab">You can replace this text</span><span>2569</span><span class="ok">✓</span><span>12%</span><span>2569</span></div>
  <div class="tbl-row" style="top:178px"><span class="lab">You can replace this text</span><span>1020</span><span class="no">✕</span><span>65%</span><span>1020</span></div>
  <div class="tbl-row" style="top:202px"><span class="lab">You can replace this text</span><span>2320</span><span class="ok">✓</span><span>36%</span><span>2320</span></div>
  <div class="tbl-row" style="top:226px"><span class="lab">You can replace this text</span><span>5698</span><span class="no">✕</span><span>95%</span><span>5698</span></div>
  <div class="tbl-row" style="top:250px"><span class="lab">You can replace this text</span><span>1999</span><span class="no">✕</span><span>66%</span><span>1999</span></div>
</div>

<div class="slide" style="left:618px;top:3184px">
  <span class="corner-mark"></span><span class="copyright">COPYRIGHT © 2021</span><span class="page-no">19</span>
  <div class="abs title" style="left:60px;top:36px;font-size:20px">Here Goes Title Of This Slide</div>
  <svg class="abs" style="left:40px;top:172px" width="500" height="20" viewBox="0 0 500 20">
    <polygon points="0,2 95,2 103,10 95,18 0,18" fill="#ec1f27"/>
    <polygon points="95,2 190,2 198,10 190,18 95,18 103,10" fill="#221f20"/>
    <polygon points="190,2 285,2 293,10 285,18 190,18 198,10" fill="#ec1f27"/>
    <polygon points="285,2 380,2 388,10 380,18 285,18 293,10" fill="#221f20"/>
    <polygon points="380,2 492,2 500,10 492,18 380,18 388,10" fill="#ec1f27"/>
  </svg>
  <span class="tl-year" style="left:102px">1990</span>
  <span class="tl-year" style="left:197px">2001</span>
  <span class="tl-year" style="left:292px">2010</span>
  <span class="tl-year" style="left:387px">2018</span>
  <span class="tl-year" style="left:482px">2021</span>
  <div class="tl-text" style="left:102px;top:118px"><h6>Your Title</h6><p class="tiny">Refers to a good or service being offered</p></div>
  <div class="tl-pin" style="left:102px;top:150px"></div>
  <div class="tl-text" style="left:292px;top:118px"><h6>Your Title</h6><p class="tiny">Refers to a good or service being offered</p></div>
  <div class="tl-pin" style="left:292px;top:150px"></div>
  <div class="tl-text" style="left:482px;top:118px"><h6>Your Title</h6><p class="tiny">Refers to a good or service being offered</p></div>
  <div class="tl-pin" style="left:482px;top:150px"></div>
  <div class="tl-pin" style="left:197px;top:192px"></div>
  <div class="tl-text" style="left:197px;top:216px"><h6>Your Title</h6><p class="tiny">Refers to a good or service being offered</p></div>
  <div class="tl-pin" style="left:387px;top:192px"></div>
  <div class="tl-text" style="left:387px;top:216px"><h6>Your Title</h6><p class="tiny">Refers to a good or service being offered</p></div>
</div>

<!-- Row 9 -->
<div class="slide" style="left:24px;top:3527px">
  <span class="corner-mark"></span><span class="copyright">COPYRIGHT © 2021</span><span class="page-no">20</span>
  <div class="abs title" style="left:60px;top:36px;font-size:20px">Here Goes Title Of This Slide</div>
  <svg class="abs" style="left:195px;top:110px" width="180" height="180" viewBox="0 0 180 180">
    <path d="M90 90 L90 2 A88 88 0 0 0 2 90 Z" fill="#221f20"/>
    <path d="M90 90 L178 90 A88 88 0 0 0 90 2 Z" fill="#ec1f27"/>
    <path d="M90 90 L90 178 A88 88 0 0 0 178 90 Z" fill="#221f20"/>
    <path d="M90 90 L2 90 A88 88 0 0 0 90 178 Z" fill="#ec1f27"/>
    <path d="M90 2 V178 M2 90 H178" stroke="#fff" stroke-width="4"/>
    <circle cx="90" cy="90" r="40" fill="#fff"/>
    <circle cx="48" cy="48" r="9" fill="none" stroke="#fff" stroke-width="1.5"/>
    <circle cx="132" cy="48" r="9" fill="none" stroke="#fff" stroke-width="1.5"/>
    <circle cx="132" cy="132" r="9" fill="none" stroke="#fff" stroke-width="1.5"/>
    <circle cx="48" cy="132" r="9" fill="none" stroke="#fff" stroke-width="1.5"/>
  </svg>
  <div class="brand center" style="left:285px;top:183px;font-size:6px;color:var(--ink)"><span class="brand-mark" style="width:10px;height:10px"></span>Korvane blockchain</div>
  <div class="pie-text" style="left:75px;top:104px;text-align:right"><h6>Your Contents Here</h6><p class="tiny">Lorem ipsum dolor sit amet, consectetur adipiscing elit, sed do eiusmod tempor incididunt.</p></div>
  <div class="pie-text" style="left:75px;top:200px;text-align:right"><h6>Your Contents Here</h6><p class="tiny">Lorem ipsum dolor sit amet, consectetur adipiscing elit, sed do eiusmod tempor incididunt.</p></div>
  <div class="pie-text" style="left:390px;top:100px"><h6>Your Contents Here</h6><p class="tiny">Lorem ipsum dolor sit amet, consectetur adipiscing elit, sed do eiusmod tempor incididunt.</p></div>
  <div class="pie-text" style="left:390px;top:198px"><h6>Your Contents Here</h6><p class="tiny">Lorem ipsum dolor sit amet, consectetur adipiscing elit, sed do eiusmod tempor incididunt.</p></div>
</div>

<div class="slide dark" style="left:618px;top:3527px">
  <div class="photo" role="img" aria-label="Dark alpine forest and mountain landscape" style="left:0;top:0;width:566px;height:319px;background:linear-gradient(180deg,#2e2d2f 0%,#3e3d40 35%,#262527 70%,#141314 100%)"></div>
  <div class="abs" style="left:52px;top:92px;font-family:Montserrat,sans-serif;font-weight:600;font-size:24px;line-height:1.2">Thank You.<br><span class="red">Contact Us.</span></div>
  <div class="contact-line" style="top:168px"><i></i>www.websitename.org</div>
  <div class="contact-line" style="top:194px"><i></i>hello@korvane-mail.example</div>
  <div class="contact-line" style="top:220px"><i></i>+00 000 000 000</div>
  <div class="contact-line" style="top:246px"><i></i>Here is a place for address</div>
  <div class="brand" style="left:280px;top:180px;font-size:22px;gap:8px"><span class="brand-mark" style="width:20px;height:20px"></span>Korvane blockchain</div>
</div>

</body>
</html>
```